Titelblatt für Masterarbeit übers Crowdsourcing
Meine Masterarbeit, von daher sollte das Design vor allen Dingen meine betreuenden Profs und natürlich auch mir selbst gefallen ;)
Hey Du ;), es geht darum die Titelseite bzw. den Umschlag meiner Masterarbeit zu designen bzw. zu gestalten.
Der Titel der Arbeit lautet: "Crowdsourcing: Beschreibung des Status Quo sowie der Möglichkeiten und Grenzen der betriebswirtschaftlich zielführenden Anwendung von Crowdsourcing für Unternehmen"
Von daher sollte sich der oben genannte Titel, sowie mein Name: Konrad Mebusch, in der Gestaltung der Titelseite wiederfinden.
Diese sollte ähnlich eines klassischen Buchs aussehen. Nur halt nicht als kompletter Umschlag, sondern nur die Frontseite.
Format DIN A4
Es wäre echt cool, wenn die Illustration in irgendeiner Art das Prinzip des Crowdsourcing symbolisieren würde bzw. zumindest die Crowd darstellt.
Ich habe zur Inspiration ein paar Links zu Bildern bzw. dem Coversourcing des Crowdsourcing Buches von Dale Brinn beigefügt:
http://studioquelm.com/blog/taking-crowdsourcing-to-its-logical-conclusion
--> hier gefallen mir eigentlich alle vorschläge, ausgenommen dem unten, aussen rechts.
http://www.pictorvo.com/photos/tags/coversourcing/
Ich freue mich echt über jeden Designvorschlag.
Herzliche Grüße
Konrad

```html
<!DOCTYPE html>
<html lang="de">
<head>
<meta charset="utf-8">
<title>Crowdsourcing – Titelblatt Masterarbeit</title>
<link rel="stylesheet" href="https://fonts.googleapis.com/css2?family=Fredoka:wght@700&family=Fira+Sans+Condensed:wght@400;600&family=Open+Sans:wght@400&display=swap">
<style>
  :root {
    --stage: #d9d9d9;
    --cover-deep: #243f8f;
    --cover-mid: #2f59b0;
    --cover-light: #5d94d3;
    --paper-white: #ffffff;
    --title-shadow: rgba(20, 30, 60, 0.45);
    --bubble-red: #b8333a;
    --bubble-yellow: #f1db7c;
    --bubble-green: #8fa83a;
    --bubble-orange: #d9913a;
    --rule: rgba(255, 255, 255, 0.55);
  }
  * { margin: 0; padding: 0; box-sizing: border-box; }
  html, body {
    width: 1200px;
    height: 900px;
    overflow: hidden;
    background: var(--stage);
  }
  .cover {
    position: absolute;
    left: 300px;
    top: 26px;
    width: 600px;
    height: 848px;
    background:
      radial-gradient(ellipse 70% 45% at 50% 38%, var(--cover-light) 0%, var(--cover-mid) 55%, var(--cover-deep) 100%);
    box-shadow: 0 10px 30px rgba(0, 0, 0, 0.25);
    color: var(--paper-white);
    overflow: hidden;
  }
  .cover__author {
    position: absolute;
    top: 56px;
    left: 0;
    right: 0;
    text-align: center;
    font-family: "Open Sans", sans-serif;
    font-size: 14px;
    letter-spacing: 1.5px;
    text-transform: uppercase;
  }
  .cover__author::after {
    content: "";
    display: block;
    width: 180px;
    height: 1px;
    margin: 7px auto 0;
    background: var(--rule);
  }
  .cover__crowd {
    position: absolute;
    left: 90px;
    top: 150px;
    width: 420px;
    height: 400px;
  }
  .cover__title {
    position: absolute;
    left: 0;
    right: 0;
    top: 262px;
    text-align: center;
    font-family: "Fredoka", sans-serif;
    font-weight: 700;
    font-size: 104px;
    line-height: 0.88;
    letter-spacing: 1px;
    text-transform: uppercase;
    transform: rotate(-6deg);
    text-shadow: 6px 8px 10px var(--title-shadow);
  }
  .cover__title span { display: block; }
  .cover__title .cover__title-line--second { margin-left: -10px; }
  .cover__subtitle {
    position: absolute;
    left: 20px;
    right: 20px;
    top: 682px;
    text-align: center;
    font-family: "Fira Sans Condensed", sans-serif;
    text-transform: uppercase;
  }
  .cover__subtitle-lead {
    font-weight: 600;
    font-size: 21px;
    letter-spacing: 0.5px;
    margin-bottom: 4px;
  }
  .cover__subtitle-rest {
    font-weight: 400;
    font-size: 15.5px;
    letter-spacing: 1.4px;
    line-height: 1.3;
  }
</style>
</head>
<body>
  <main class="cover">
    <p class="cover__author">Konrad Mebusch</p>

    <svg class="cover__crowd" viewBox="0 0 420 400" role="img" aria-label="Illustration: dichte Wolke bunter Sprechblasen in Rot, Gelb, Grün und Orange als Symbol für die Crowd">
      <defs>
        <radialGradient id="crowd-tones" cx="50%" cy="50%" r="50%">
          <stop offset="0%" stop-color="var(--bubble-yellow)" stop-opacity="0.85"/>
          <stop offset="40%" stop-color="var(--bubble-red)" stop-opacity="0.75"/>
          <stop offset="75%" stop-color="var(--bubble-orange)" stop-opacity="0.55"/>
          <stop offset="100%" stop-color="var(--bubble-green)" stop-opacity="0"/>
        </radialGradient>
      </defs>
      <ellipse cx="210" cy="200" rx="210" ry="200" fill="url(#crowd-tones)"/>
    </svg>

    <h1 class="cover__title">
      <span class="cover__title-line">Crowd-</span>
      <span class="cover__title-line cover__title-line--second">Sourcing</span>
    </h1>

    <div class="cover__subtitle">
      <p class="cover__subtitle-lead">Beschreibung des Status Quo</p>
      <p class="cover__subtitle-rest">sowie der Möglichkeiten und Grenzen der betriebswirtschaftlich<br>zielführenden Anwendung von Crowdsourcing für Unternehmen</p>
    </div>
  </main>
</body>
</html>
```